Travel Blogger Business Card for roamquill.net

I need a two-sided business card for a travel blogging website. The card should be both professional and fun at the same time. This is for the website www.roamquill.net

I don't necessarily think that the current logo on the website needs to be used on the business card but it can be. I am very flexible with ideas

Target Market(s)

Travel agencies that will be met at a conference.

Industry/Entity Type

Travel

Contact Information for Business Card

Company Name: Roam Quill.net
Name: Bertrand Olesky
Voice: +1-(345)-402-7731
Address: Coral Reach Shore, Grand Cayman, Cayman Islands
Email: ceo@roamquill.net

Colors
0592cd
0355a3
3176b5
33a6d7
85cae6
85acd3

Requirements
Must have
• Website address and name should be bigger than address, phone number, and email.

```html
<!DOCTYPE html>
<html lang="en">
<head>
<meta charset="utf-8">
<title>Roam Quill.net – Business Card</title>
<link href="https://fonts.googleapis.com/css2?family=Arimo:wght@400;700&display=swap" rel="stylesheet">
<style>
  :root {
    --backdrop: #2b2a28;
    --brand-blue: #26519b;
    --paper: #ffffff;
    --ink: #2e2e2e;
    --rule: #3a3a3a;
    --symbol-light: #eef0f3;
    --symbol-mid: #c9ced6;
  }
  * { margin: 0; padding: 0; box-sizing: border-box; }
  html, body {
    width: 986px; height: 1200px; overflow: hidden;
    background: var(--backdrop);
    font-family: "Arimo", Arial, sans-serif;
  }
  .card {
    position: absolute; left: 83px; width: 819px; height: 466px;
  }
  .card--front { top: 100px; background: var(--paper); }
  .card--back { top: 633px; background: var(--brand-blue); }

  .web-tab {
    position: absolute; display: flex; align-items: center; justify-content: center;
    font-weight: 700; font-size: 27px;
  }
  .card--front .web-tab {
    left: 59px; top: 0; width: 327px; height: 61px;
    background: var(--brand-blue); color: var(--paper);
    border-radius: 0 0 20px 20px;
  }
  .card--back .web-tab {
    left: 433px; bottom: 0; width: 328px; height: 61px;
    background: var(--paper); color: var(--brand-blue);
    border-radius: 20px 20px 0 0; font-size: 25px;
  }

  .brand-symbol {
    position: absolute; left: 128px; top: 158px; width: 180px; height: 156px;
    background: radial-gradient(ellipse at center, var(--symbol-light) 0%, var(--symbol-mid) 100%);
    border-radius: 6px;
  }

  .holder-name {
    position: absolute; left: 398px; top: 138px;
    color: var(--brand-blue); font-weight: 700; font-size: 42px; letter-spacing: -0.5px;
  }
  .contact {
    position: absolute; left: 398px; top: 240px;
    color: var(--ink); font-size: 31px; line-height: 43px;
  }
  .divider {
    position: absolute; left: 62px; top: 406px; width: 694px; height: 2px;
    background: var(--rule);
  }
  .address {
    position: absolute; left: 73px; top: 418px;
    color: var(--ink); font-size: 28px;
  }

  .brand-lockup {
    position: absolute; left: 112px; top: 210px;
    display: flex; align-items: center; gap: 22px;
  }
  .brand-dot {
    width: 64px; height: 64px; border-radius: 50%; background: var(--paper);
  }
  .brand-name {
    color: var(--paper); font-weight: 700; font-size: 58px; letter-spacing: 0.5px;
  }
</style>
</head>
<body>
  <section class="card card--front">
    <div class="web-tab">roamquill.net</div>
    <div class="brand-symbol" role="img" aria-label="Brand symbol area"></div>
    <h1 class="holder-name">BERTRAND OLESKY</h1>
    <p class="contact">+1-(345)-402-7731<br>ceo@roamquill.net</p>
    <div class="divider"></div>
    <p class="address">Coral Reach Shore, Grand Cayman, Cayman Islands</p>
  </section>

  <section class="card card--back">
    <div class="brand-lockup">
      <span class="brand-dot"></span>
      <span class="brand-name">ROAM QUILL.NET</span>
    </div>
    <div class="web-tab">www.roamquill.net</div>
  </section>
</body>
</html>
```